New name flyer

We have just changed our business name from kR Property group to Harbour Lantern. We want to distribute a flyer to the local community to inform them of the change. We are a realestate agency which focuses mainly on property management but also sales. We service from Brisbane to the Sunshine coast.

Target Market(s)

Local community

Industry/Entity Type

realestate

Requirements
Must have
• Details of name change
Nice to have
• Servicing area Brisbane and Sunshine Coast, no change in management or services we offer, and will continue pride ourselves on offering a high level of service, with the same team from the Gold to Sunshine Coast.
Should not have
• too much wording.

```html
<!DOCTYPE html>
<html lang="en">
<head>
<meta charset="utf-8">
<title>Harbour Lantern – Change of Company Name</title>
<link href="https://fonts.googleapis.com/css2?family=Roboto+Condensed:wght@300;400;700&family=Nunito+Sans:ital,wght@0,400;0,600;1,400&display=swap" rel="stylesheet">
<style>
  :root {
    --navy-deep: #07133d;
    --navy-mid: #0c2684;
    --gold: #c9962a;
    --white: #ffffff;
    --photo-sky: #efd9e6;
    --photo-sea: #4f7f8f;
  }
  * { margin: 0; padding: 0; box-sizing: border-box; }
  html, body { width: 849px; height: 1200px; overflow: hidden; background: var(--navy-deep); }
  .flyer {
    position: relative;
    width: 849px;
    height: 1200px;
    overflow: hidden;
    background: radial-gradient(ellipse 70% 55% at 62% 48%, var(--navy-mid) 0%, #0a1c62 45%, var(--navy-deep) 100%);
    font-family: "Roboto Condensed", "Arial Narrow", sans-serif;
    color: var(--white);
  }
  .coast-photo {
    position: absolute;
    left: 0; top: 158px;
    width: 257px; height: 884px;
    background: linear-gradient(180deg, var(--photo-sky) 0%, #e9d3e0 38%, #9aa3ad 55%, #6f8592 75%, var(--photo-sea) 88%, #2f5a6b 100%);
  }
  .photo-credit {
    font-family: "Nunito Sans", sans-serif;
    font-size: 11px;
    letter-spacing: 0.5px;
    color: var(--gold);
    white-space: nowrap;
  }
  .photo-credit strong { font-weight: 600; }
  .photo-credit em { font-style: italic; }
  .coast-credit {
    position: absolute;
    left: 40px; top: 460px;
    transform: rotate(-90deg);
    transform-origin: 0 0;
  }
  .brand {
    position: absolute;
    left: 372px; top: 185px;
    display: flex;
    align-items: center;
    gap: 16px;
  }
  .brand-square { width: 22px; height: 22px; background: var(--white); }
  .brand-name {
    font-weight: 300;
    font-size: 52px;
    letter-spacing: 1px;
    color: var(--white);
    text-transform: uppercase;
    line-height: 1;
  }
  .headline {
    position: absolute;
    left: 300px; width: 500px;
    text-align: center;
    font-weight: 700;
    line-height: 1.1;
  }
  .announce { top: 376px; font-size: 46px; color: var(--gold); }
  .change-title { top: 446px; font-size: 29px; color: var(--white); }
  .old-name { top: 520px; font-size: 28px; color: var(--white); }
  .new-name { top: 557px; font-size: 29px; color: var(--gold); }
  .body-copy {
    position: absolute;
    left: 321px; width: 453px;
    font-weight: 300;
    font-size: 18.5px;
    line-height: 24px;
    text-align: justify;
  }
  .body-copy strong { font-weight: 700; }
  .body-copy .gold { color: var(--gold); }
  .intro { top: 650px; }
  .promise { top: 770px; }
  .city-photo {
    position: absolute;
    left: 484px; top: 908px;
    width: 290px; height: 186px;
    background: linear-gradient(180deg, #2c7fd0 0%, #5fa6e2 40%, #c2b9a3 60%, #556a4c 75%, #1f5f8f 100%);
  }
  .city-credit { position: absolute; left: 484px; top: 1118px; }
  .website {
    position: absolute;
    left: 45px; top: 1115px;
    font-family: "Nunito Sans", sans-serif;
    font-size: 14px;
    letter-spacing: 1.8px;
    color: var(--white);
  }
  .footer-mark {
    position: absolute;
    left: 334px; top: 1112px;
    width: 22px; height: 22px;
    border: 1.5px solid var(--white);
  }
</style>
</head>
<body>
  <main class="flyer">
    <div class="coast-photo" role="img" aria-label="Aerial view of coastal high-rise towers beside the beach and surf"></div>
    <p class="photo-credit coast-credit">photo by : <strong>Coastline Studio</strong> <em>(stockfolio)</em></p>

    <div class="brand">
      <span class="brand-name">Harbour Lantern</span>
      <span class="brand-square"></span>
    </div>

    <h1 class="headline announce">ANNOUCEMENT!</h1>
    <h2 class="headline change-title">CHANGE OF COMPANY NAME:</h2>
    <p class="headline old-name">kR Property -</p>
    <p class="headline new-name">HARBOUR LANTERN ESTATE AGENTS</p>

    <p class="body-copy intro">We are a REAL ESTATE AGENCY and had recently changed our company name - <strong>kR Property group</strong> to <strong class="gold">Harbour Lantern Estate Agents</strong>. We focuses mainly on Property Management and Property Sales.</p>
    <p class="body-copy promise">There will be NO CHANGE IN MANAGEMENT or SERVICES and we continue to pride ourselves on offering a high level of service, with the same team from the Brisbane - Gold Coast to Sunshine Coast.</p>

    <div class="city-photo" role="img" aria-label="City skyline across the river with boats on the water"></div>
    <p class="photo-credit city-credit">photo by : <strong>River City Lens</strong> <em>(stockfolio)</em></p>

    <p class="website">www.harbourlantern.au</p>
    <span class="footer-mark"></span>
  </main>
</body>
</html>
```